TOBREL Business Card Design

We need a business card design for a current Plastering company now moving to building and constructing new homes.
We have been in the Plastering(rendering) business for 15yrs and have made a good name with our customers for our Top Quality of work that we provide.
We would like TOBREL to be the main attraction with an image of architectural roof tops or house design within it. Blue Yellow and Black are colours we like but are willing to see other ideas.
We would like the design to be modern and communicate quality and experience.
Industry/Entity Type
Building
Contact Information for Business Card
TOBREL Building and Plastering
PO BOX 73519 Casuarina Darwin NT 0812
PH/Fax: 08 83170925 Email: tobrel@wavemail.example
Glen: 0419372654 Ruth:0408631597
ABN:57 208 931 446

```html
<!DOCTYPE html>
<html lang="en">
<head>
<meta charset="utf-8">
<title>TOBREL Building and Plastering – Business Card</title>
<link href="https://fonts.googleapis.com/css2?family=Source+Sans+3:wght@400;600;700&display=swap" rel="stylesheet">
<style>
  :root {
    --ink: #1c1c1c;
    --paper: #ffffff;
    --wall-shadow: #dcd9d5;
    --wall-mid: #e9e7e4;
    --wall-light: #f4f3f2;
    --mark-tone: #d9d5cf;
  }
  html, body {
    margin: 0;
    padding: 0;
    width: 1200px;
    height: 741px;
    overflow: hidden;
    background: var(--paper);
  }
  .card {
    position: relative;
    width: 1200px;
    height: 741px;
    overflow: hidden;
    font-family: "Source Sans 3", "Myriad Pro", Arial, sans-serif;
    color: var(--ink);
    background: var(--paper);
  }
  .card__photo {
    position: absolute;
    inset: 0;
    width: 1200px;
    height: 741px;
  }
  .brand-mark {
    position: absolute;
    left: 880px;
    top: 430px;
    width: 230px;
    display: flex;
    flex-direction: column;
    align-items: center;
    gap: 22px;
  }
  .brand-mark__square {
    width: 96px;
    height: 96px;
    background: var(--mark-tone);
  }
  .brand-mark__name {
    margin: 0;
    font-size: 60px;
    font-weight: 600;
    line-height: 1;
    letter-spacing: 2px;
    color: var(--mark-tone);
  }
  .card__text {
    position: absolute;
    left: 67px;
    top: 0;
  }
  .line {
    position: absolute;
    left: 0;
    margin: 0;
    line-height: 1;
    white-space: nowrap;
  }
  .company-name { top: 180px; font-size: 58px; font-weight: 400; letter-spacing: 0.5px; }
  .company-trade { top: 239px; font-size: 44px; font-weight: 400; }
  .company-abn { top: 291px; font-size: 31px; font-weight: 700; letter-spacing: 0.8px; }
  .address { top: 347px; font-size: 45px; font-weight: 400; }
  .address--second { top: 394px; }
  .contact {
    display: grid;
    grid-template-columns: 162px auto;
    font-size: 44px;
  }
  .contact__label { font-weight: 700; }
  .contact__value { font-weight: 400; }
  .contact--phone { top: 458px; }
  .contact--email { top: 516px; }
  .contact--glen { top: 575px; }
  .contact--ruth { top: 633px; }
</style>
</head>
<body>
  <div class="card">
    <svg class="card__photo" viewBox="0 0 1200 741" xmlns="http://www.w3.org/2000/svg">
      <defs>
        <linearGradient id="wallTone" x1="0" y1="0" x2="1" y2="0.6">
          <stop offset="0" stop-color="var(--wall-mid)"/>
          <stop offset="0.45" stop-color="var(--wall-shadow)"/>
          <stop offset="0.62" stop-color="var(--wall-mid)"/>
          <stop offset="1" stop-color="var(--wall-light)"/>
        </linearGradient>
      </defs>
      <rect role="img" aria-label="Photograph of a smooth white rendered plaster interior with angled walls and soft window light"
            x="0" y="0" width="1200" height="741" fill="url(#wallTone)"/>
      <polygon class="card__panel" points="0,0 162,0 787,479 787,741 0,741" fill="var(--paper)"/>
    </svg>

    <div class="brand-mark">
      <div class="brand-mark__square"></div>
      <p class="brand-mark__name">TOBREL</p>
    </div>

    <div class="card__text">
      <p class="line company-name">TOBREL</p>
      <p class="line company-trade">Building and Plastering</p>
      <p class="line company-abn">ABN:57 208 931 446</p>
      <p class="line address">PO BOX 73519 Casuarina</p>
      <p class="line address address--second">Darwin NT 0812</p>
      <p class="line contact contact--phone"><span class="contact__label">PH/Fax:</span><span class="contact__value">08 83170925</span></p>
      <p class="line contact contact--email"><span class="contact__label">Email:</span><span class="contact__value">tobrel@wavemail.example</span></p>
      <p class="line contact contact--glen"><span class="contact__label">Glen:</span><span class="contact__value">0419372654</span></p>
      <p class="line contact contact--ruth"><span class="contact__label">Ruth:</span><span class="contact__value">0408631597</span></p>
    </div>
  </div>
</body>
</html>
```